Business Card Design

The Wren Lodge Motel is the most centrally located motel in Grafton.
We are the only family owned motel in Grafton.
Our colour scheme is blue, whiteand black.
Updates

I have uploaded a photo of our new rooms and the logo for you to use Thanks. Looking good

Industry/Entity Type

Motel

Contact Information for Business Card

The Wren Lodge Motel
Colin & Maree Tulloch
Owner/Operators
14-16 Barwell Road, Grafton NSW 2460
Ph: 02 6613 4879
Email: thewrenlodgemotel@mailbay.example
reception@wrenlodgemotel.example
www.wrenlodgemotel.example

Colors
0392cd
0455a3

```html
<!DOCTYPE html>
<html lang="en">
<head>
<meta charset="utf-8">
<title>The Wren Lodge Motel – Business Card</title>
<link href="https://fonts.googleapis.com/css2?family=Comfortaa:wght@400;700&display=swap" rel="stylesheet">
<style>
  :root {
    --page-bg: #e4e4e6;
    --card-bg: #f1f1f3;
    --band-light: #6662b4;
    --band-dark: #3f3b98;
    --accent: #4a46a2;
    --ink: #2a2a30;
    --white: #ffffff;
    --sign-fill: #dcdcea;
  }
  * { margin: 0; padding: 0; box-sizing: border-box; }
  html, body { width: 1200px; height: 750px; overflow: hidden; }
  body {
    background: var(--page-bg);
    font-family: "Comfortaa", sans-serif;
    position: relative;
  }
  .card {
    position: absolute;
    left: 150px; top: 105px;
    width: 900px; height: 540px;
    border-radius: 44px;
    background: var(--card-bg);
    overflow: hidden;
    box-shadow: 0 10px 30px rgba(0,0,0,0.12);
  }
  .card__band { position: absolute; inset: 0; width: 900px; height: 540px; }
  .card__sign {
    position: absolute;
    left: 690px; top: 28px;
    width: 170px; height: 120px;
    background: var(--sign-fill);
    border-radius: 6px;
  }
  .brand {
    position: absolute;
    left: 70px; top: 105px;
    color: var(--white);
    font-weight: 700;
    line-height: 1.1;
  }
  .brand__line1 { font-size: 56px; display: block; }
  .brand__line2 { font-size: 36px; display: block; margin: 6px 0 0 290px; }
  .owners { position: absolute; left: 80px; top: 392px; }
  .owners__names { color: var(--accent); font-size: 30px; font-weight: 700; }
  .owners__role { color: var(--ink); font-size: 20px; margin-top: 10px; }
  .contact-row {
    display: flex; align-items: center; gap: 12px;
    color: var(--accent); font-size: 19px; font-weight: 700;
  }
  .contact-row svg { flex: none; }
  .owners .contact-row { margin-top: 22px; }
  .location { position: absolute; left: 612px; top: 272px; }
  .location .contact-row { align-items: flex-start; line-height: 1.35; }
  .location .contact-row + .contact-row { margin-top: 14px; align-items: center; }
</style>
</head>
<body>
  <div class="card">
    <svg class="card__band" viewBox="0 0 900 540" aria-hidden="true">
      <defs>
        <linearGradient id="bandGrad" x1="0" y1="0" x2="1" y2="0">
          <stop offset="0" stop-color="var(--band-light)"/>
          <stop offset="1" stop-color="var(--band-dark)"/>
        </linearGradient>
      </defs>
      <path d="M0 0 H900 V200 C700 240 400 290 0 370 Z" fill="url(#bandGrad)"/>
    </svg>

    <div class="card__sign" role="img" aria-label="Illustration of a roadside motel sign with vacancy panel"></div>

    <div class="brand">
      <span class="brand__line1">The Wren Lodge</span>
      <span class="brand__line2">Motel</span>
    </div>

    <div class="location">
      <div class="contact-row">
        <svg width="20" height="20" viewBox="0 0 20 20" aria-hidden="true"><circle cx="10" cy="10" r="10" fill="var(--ink)"/><path d="M10 4a4 4 0 0 0-4 4c0 3 4 8 4 8s4-5 4-8a4 4 0 0 0-4-4zm0 5.5a1.5 1.5 0 1 1 0-3 1.5 1.5 0 0 1 0 3z" fill="var(--white)"/></svg>
        <span>14-16 Barwell Road,<br>Grafton NSW 2460</span>
      </div>
      <div class="contact-row">
        <svg width="20" height="20" viewBox="0 0 20 20" aria-hidden="true"><circle cx="10" cy="10" r="10" fill="var(--ink)"/><path d="M7 5l2 2.5-1.2 1.3a7 7 0 0 0 3.4 3.4L12.5 11 15 13l-1 2c-4 0-9-5-9-9z" fill="var(--white)"/></svg>
        <span>02 6613 4879</span>
      </div>
    </div>

    <div class="owners">
      <div class="owners__names">Colin &amp; Maree Tulloch</div>
      <div class="owners__role">Owner/Operators</div>
      <div class="contact-row">
        <svg width="20" height="20" viewBox="0 0 20 20" aria-hidden="true"><circle cx="10" cy="10" r="10" fill="var(--ink)"/><rect x="5" y="6.5" width="10" height="7" rx="1" fill="var(--white)"/><path d="M5.5 7l4.5 3.5L14.5 7" stroke="var(--ink)" stroke-width="1" fill="none"/></svg>
        <span>thewrenlodgemotel@mailbay.example</span>
      </div>
    </div>
  </div>
</body>
</html>
```